One page website for a Personal Injury Law Firm

Design and code a one page website in WordPress for the Darrow Law Firm, which is a a personal injury law firm located in Coral Gables, Florida. Please note: if you want to change the color pallete for the logo and for the web design , that is fine by me.

Target Market(s)

Those injured in accidents that need legal representation

Industry/Entity Type

Legal

Coding

Coded - Design and coding required

Number of Pages Required

1 page

Font styles to use
Other font styles liked:
• Montserrat

```html
<!DOCTYPE html>
<html lang="en">
<head>
<meta charset="utf-8">
<title>Darrow Law Firm | Personal Injury Representation</title>
<link href="https://fonts.googleapis.com/css2?family=Montserrat:wght@400;500;600;700;800&display=swap" rel="stylesheet">
<style>
:root{
  --gold:#d2a36f;
  --gold-soft:#d9b487;
  --dark:#303030;
  --ink:#2b2b2b;
  --muted:#5c5c5c;
  --white:#ffffff;
}
*{margin:0;padding:0;box-sizing:border-box}
html,body{width:1200px;height:4461px;overflow:hidden}
body{font-family:'Montserrat',sans-serif;color:var(--ink);background:var(--white);position:relative}
.gold{color:var(--gold)}
.img-fill{position:absolute}

/* header */
.site-header{position:absolute;left:0;top:0;width:1200px;height:78px;background:var(--white)}
.brand{position:absolute;left:100px;top:24px;display:flex;align-items:center;gap:10px;font-weight:700;font-size:22px;color:var(--ink);white-space:nowrap}
.brand .dot{width:14px;height:14px;background:var(--gold)}
.main-nav{position:absolute;left:404px;top:31px;display:flex;font-size:10.5px;font-weight:600;letter-spacing:.3px;white-space:nowrap}
.main-nav span{padding:0 20px;border-left:1px solid #ccc}
.main-nav span:first-child{border-left:none;padding-left:0}

/* hero */
.hero{position:absolute;left:0;top:78px;width:1200px;height:732px;background:linear-gradient(135deg,#3a2a17 0%,#7a5a30 35%,#a8844d 55%,#4a3720 80%,#261b10 100%)}
.hero-title{position:absolute;left:0;top:252px;width:1200px;text-align:center;color:var(--white);font-weight:800;font-size:96px;line-height:90px;letter-spacing:-1px}
.hero-sub{position:absolute;left:0;top:454px;width:1200px;text-align:center;color:var(--white);font-weight:700;font-size:15.5px}
.hero-arrow{position:absolute;top:315px;width:48px;height:108px;background:rgba(40,40,40,.55);display:flex;align-items:center;justify-content:center}
.mouse{position:absolute;left:591px;top:660px;width:18px;height:28px;border:2px solid var(--white);border-radius:10px}
.mouse::after{content:"";position:absolute;left:6px;top:5px;width:2px;height:7px;background:var(--white)}

/* intro */
.intro{position:absolute;left:0;top:810px;width:1200px;height:440px;background:var(--dark);color:#ddd}
.intro-mark{position:absolute;left:150px;top:110px;width:330px;height:200px;display:flex;align-items:center;justify-content:center;gap:12px;color:var(--gold);font-weight:700;font-size:28px;white-space:nowrap}
.intro-mark .dot{width:18px;height:18px;background:var(--gold)}
.intro h2{position:absolute;left:495px;top:80px;color:var(--white);font-size:25px;font-weight:700;line-height:30px;white-space:nowrap}
.intro p{position:absolute;left:495px;width:460px;font-size:11px;line-height:15.5px;color:#cfcfcf}
.contact-chip{position:absolute;top:338px;display:flex;align-items:center;gap:10px;font-size:10px;font-weight:600;color:var(--white);white-space:nowrap}
.chip-icon{width:28px;height:28px;background:var(--gold);border-radius:50%;display:flex;align-items:center;justify-content:center}

/* why */
.section-title{font-size:26px;font-weight:700;line-height:30px;color:var(--ink);white-space:nowrap}
.why-title{position:absolute;left:175px;top:1353px}
.why-sub{position:absolute;left:175px;top:1427px;font-size:11px;color:var(--muted)}
.feature{position:absolute;left:175px;width:460px;display:flex;gap:14px}
.feature svg{flex:none}
.feature h3{font-size:11px;font-weight:700;margin-bottom:4px}
.feature p{font-size:10.5px;line-height:15px;color:var(--muted)}
.case-notes{position:absolute;left:594px;top:1826px;width:405px}
.case-notes p{font-size:11px;line-height:15.5px;color:var(--muted);margin-bottom:13px}

/* strategy */
.strategy{position:absolute;left:0;top:2260px;width:1200px;height:400px;background:var(--dark)}
.strategy h2{position:absolute;left:0;top:80px;width:1200px;text-align:center;color:var(--white);font-size:27px;font-weight:700;line-height:33px}
.pillar{position:absolute;top:185px;display:flex;gap:22px}
.pillar h3{font-size:11px;font-weight:700;color:var(--white);line-height:15px;margin-bottom:8px}
.pillar p{font-size:10.5px;line-height:15px;color:#cfcfcf;width:172px}
.pillar-divider{position:absolute;top:185px;width:1px;height:155px;background:#4a4a4a}

/* practice */
.practice-title{position:absolute;left:165px;top:2735px}
.practice-sub{position:absolute;left:165px;top:2772px;font-size:11px;color:var(--muted)}
.slider-btn{position:absolute;top:2750px;width:28px;height:28px;border-radius:50%;display:flex;align-items:center;justify-content:center}
.card{position:absolute;top:2816px;width:276px;height:367px;background:var(--white);box-shadow:0 6px 18px rgba(0,0,0,.08)}
.card .photo{height:235px}
.card h3{position:absolute;left:23px;top:262px;font-size:11px;font-weight:700}
.card p{position:absolute;left:23px;top:286px;width:232px;font-size:10.5px;line-height:15px;color:var(--muted)}

/* florida */
.fl-title{position:absolute;left:657px;top:3310px;font-size:27px;line-height:30px}
.fl-sub{position:absolute;left:657px;top:3418px;font-size:11px;color:var(--muted)}
.law-item{position:absolute;left:657px;width:414px}
.law-item h3{display:flex;align-items:center;gap:9px;font-size:11px;font-weight:700;margin-bottom:9px;white-space:nowrap}
.law-item p{padding-left:26px;font-size:10.5px;line-height:15px;color:var(--muted)}
.rule{position:absolute;left:683px;width:388px;height:1px;background:#bdbdbd}

/* footer */
.footer{position:absolute;left:0;top:4036px;width:1200px;height:425px;background:var(--dark);color:#cfcfcf}
.cta{position:absolute;left:179px;top:3910px;width:842px;height:173px;background:var(--gold);z-index:2}
.cta-mark{position:absolute;left:76px;top:40px;width:110px;height:96px;display:flex;align-items:center;justify-content:center}
.cta h2{position:absolute;left:211px;top:44px;color:var(--white);font-size:26px;font-weight:700;white-space:nowrap}
.cta .tag{position:absolute;left:211px;top:78px;color:var(--white);font-size:11px;font-weight:700}
.cta p{position:absolute;left:211px;top:104px;width:500px;color:var(--white);font-size:10px;line-height:15px}
.foot-brand{position:absolute;left:130px;top:155px;width:314px;text-align:center}
.foot-brand .name{display:flex;align-items:center;justify-content:center;gap:10px;font-size:28px;font-weight:700;color:var(--white);white-space:nowrap}
.foot-brand .name i{width:14px;height:14px;background:var(--gold);display:block}
.foot-brand .tagline{margin-top:40px;font-size:9px;font-weight:700;color:var(--white);white-space:nowrap}
.foot-col h4{color:var(--white);font-size:14px;font-weight:700;margin-bottom:22px}
.foot-contact{position:absolute;left:494px;top:140px}
.foot-contact .row{display:flex;gap:12px;margin-bottom:18px;font-size:10.5px;line-height:15px}
.foot-links{position:absolute;left:822px;top:140px;width:240px}
.foot-links div{font-size:10.5px;padding-bottom:12px;margin-bottom:12px;border-bottom:1px solid #474747}
.copyright{position:absolute;left:0;top:388px;width:1200px;text-align:center;font-size:10.5px;color:#d8d8d8}
.to-top{position:absolute;left:1121px;top:340px;width:52px;height:52px;border-radius:50%;background:var(--gold);display:flex;align-items:center;justify-content:center}
</style>
</head>
<body>

<header class="site-header">
  <div class="brand"><span class="dot"></span>Darrow Law Firm</div>
  <nav class="main-nav">
    <span>ABOUT</span><span>WHY CHOOSE</span><span>OUR STRATEGY</span><span>OUR PRACTICE AREAS</span><span>FLORIDA PERSONAL INJURY LAW</span>
  </nav>
</header>

<section class="hero" role="img" aria-label="Low-angle view of classical courthouse columns and ornate coffered ceiling in warm golden light">
  <div class="hero-arrow" style="left:0"><svg width="12" height="12" viewBox="0 0 12 12"><path d="M8 1 3 6l5 5" stroke="#fff" stroke-width="2" fill="none"/></svg></div>
  <div class="hero-arrow" style="left:1152px"><svg width="12" height="12" viewBox="0 0 12 12"><path d="m4 1 5 5-5 5" stroke="#fff" stroke-width="2" fill="none"/></svg></div>
  <h1 class="hero-title">THE <span class="gold">DARROW</span><br>LAW FIRM</h1>
  <div class="hero-sub">CONCIERGE-LEVEL PERSONAL INJURY REPRESENTATION IN MIAMI, FLORIDA</div>
  <div class="mouse"></div>
</section>

<section class="intro" id="about">
  <div class="intro-mark"><span class="dot"></span>Darrow Law Firm</div>
  <h2>JUSTICE. RECOVERY.<br>A BETTER <span class="gold">FUTURE</span> STARTS HERE.</h2>
  <p style="top:153px">At The Darrow Law Firm, we understand that suffering a personal injury can be life-altering—physically, emotionally, and financially. You may be unsure whether pursuing legal action is the right step. But in Florida, holding negligent parties accountable isn't just your right—it's often necessary to rebuild your life.</p>
  <p style="top:233px">We take a concierge-style approach to personal injury law, offering personalized attention, strategic advocacy, and relentless dedication to securing the maximum compensation you deserve. Our mission is not only to make you whole again but to help you build a brighter future—ensuring access to the best medical care, financial stability, and peace of mind for you and your loved ones.</p>
  <div class="contact-chip" style="left:495px"><span class="chip-icon"><svg width="13" height="13" viewBox="0 0 24 24"><path d="M6.6 10.8a15 15 0 0 0 6.6 6.6l2.2-2.2a1 1 0 0 1 1-.25 11.4 11.4 0 0 0 3.6.57 1 1 0 0 1 1 1V20a1 1 0 0 1-1 1A17 17 0 0 1 3 4a1 1 0 0 1 1-1h3.5a1 1 0 0 1 1 1c0 1.25.2 2.45.57 3.6a1 1 0 0 1-.25 1z" fill="#fff"/></svg></span>Free Consultation: (786) 555-0190</div>
  <div class="contact-chip" style="left:717px"><span class="chip-icon"><svg width="13" height="13" viewBox="0 0 24 24"><path d="M3 5h18v14H3z" fill="#fff"/><path d="m3 5 9 7 9-7" stroke="#d2a36f" stroke-width="2" fill="none"/></svg></span>Email: info@darrowlawfirm.com</div>
</section>

<section id="why-choose">
  <h2 class="section-title why-title">WHY CHOOSE THE <span class="gold">DARROW</span><br>LAW FIRM?</h2>
  <div class="why-sub">Unmatched Experience. Proven Results. Relentless Advocacy.</div>

  <div class="feature" style="top:1472px">
    <svg width="36" height="40" viewBox="0 0 36 40"><circle cx="18" cy="16" r="12" fill="none" stroke="#d2a36f" stroke-width="1.6"/><circle cx="18" cy="16" r="7" fill="none" stroke="#d2a36f" stroke-width="1.3"/><path d="M11 26 8 38l5-3 3 4 2-10M25 26l3 12-5-3-3 4-2-10" fill="none" stroke="#d2a36f" stroke-width="1.3"/></svg>
    <div><h3>25+ YEARS OF LEGAL MASTERY</h3><p>We have successfully handled thousands of cases, fighting both for and against insurance companies. This unique dual experience gives us an insider advantage in every case we take on.</p></div>
  </div>
  <div class="feature" style="top:1563px">
    <svg width="36" height="40" viewBox="0 0 36 40"><path d="M18 3 31 8v11c0 9-6 15-13 18C11 34 5 28 5 19V8z" fill="none" stroke="#d2a36f" stroke-width="1.6"/><path d="m12 20 5 5 8-9" fill="none" stroke="#d2a36f" stroke-width="1.8"/></svg>
    <div><h3>EXTENSIVE KNOWLEDGE OF INSURANCE TACTICS</h3><p>Having worked for insurance companies, we know their strategies, loopholes, and how to dismantle their defenses to maximize your settlement.</p></div>
  </div>
  <div class="feature" style="top:1647px">
    <svg width="36" height="40" viewBox="0 0 36 40"><circle cx="18" cy="20" r="14" fill="none" stroke="#d2a36f" stroke-width="1.6"/><circle cx="18" cy="20" r="9" fill="none" stroke="#d2a36f" stroke-width="1.2"/><text x="18" y="24.5" text-anchor="middle" font-family="Montserrat,sans-serif" font-size="12" font-weight="700" fill="#d2a36f">$</text></svg>
    <div><h3>MILLIONS RECOVERED FOR CLIENTS</h3><p>Our track record includes life-changing results.</p></div>
  </div>

  <div class="img-fill" role="img" aria-label="Glass skyscrapers seen from below against a pale sky" style="left:667px;top:1323px;width:328px;height:422px;background:linear-gradient(160deg,#c9ccd0 0%,#5b5f64 40%,#2a2c2f 70%,#6e5335 100%)"></div>

  <div class="img-fill" role="img" aria-label="Attorney in a dark suit reviewing documents at a desk beside a small brass scale" style="left:175px;top:1765px;width:362px;height:390px;background:linear-gradient(135deg,#8a8a88 0%,#4a4b4d 45%,#23262b 100%)"></div>

  <div class="case-notes">
    <p>A client fell eight feet at a major sporting venue and suffered catastrophic injuries. We recovered compensation that covered all medical bills, paid off their home, and funded their children's college education.</p>
    <p>A client suffered a severe infection from a minor slip-and-fall injury in a Miami condo building. We resolved the case before filing a lawsuit, securing funds that allowed him to buy a new home, pay off debts, and provide private school tuition for his children.</p>
    <p>A fast-food restaurant's napkin dispenser fell on a customer's face, breaking her nose and leaving her permanently disfigured. We secured a settlement that covered plastic surgery, home renovations, and her daughter's college tuition.</p>
    <p>These are just a few examples of how we fight for our clients' futures—not just their cases.</p>
  </div>
  <div class="img-fill" role="img" aria-label="Carved stone relief on a classical courthouse pediment" style="left:825px;top:2020px;width:375px;height:240px;clip-path:polygon(100% 0,100% 100%,0 100%);background:linear-gradient(135deg,#e8e0d2 30%,#9b8f7c 65%,#5a5043 100%)"></div>
</section>

<section class="strategy" id="strategy">
  <h2>OUR STRATEGY: AGGRESSIVE,<br>CLIENT-FOCUSED, AND RESULTS-DRIVEN</h2>
  <div class="pillar" style="left:103px">
    <svg width="92" height="104" viewBox="0 0 92 104"><path d="M46 2 90 27v50L46 102 2 77V27z" fill="#d9b487"/><g fill="none" stroke="#fff" stroke-width="2"><path d="M30 72V38h32v34M26 72h40M46 30v8"/><path d="M37 46h6M49 46h6M37 55h6M49 55h6M42 72v-9h8v9"/></g></svg>
    <div><h3>TAKING ON CORPORATE<br>GIANT</h3><p>We don't back down from big insurance companies, property management firms, or major corporations. We fight for justice—no matter how powerful the opposition.</p></div>
  </div>
  <div class="pillar-divider" style="left:412px"></div>
  <div class="pillar" style="left:459px">
    <svg width="92" height="104" viewBox="0 0 92 104"><path d="M46 2 90 27v50L46 102 2 77V27z" fill="#d9b487"/><g fill="none" stroke="#fff" stroke-width="2"><path d="M46 28v36M32 36h28M32 36l-6 14h12zM60 36l-6 14h12zM38 64h16"/><path d="M24 70c8 6 16 8 26 6l16-6"/></g></svg>
    <div><h3>CONCIERGE-STYLE<br>LEGAL CARE</h3><p>You're not just another case number. We provide dedicated, personalized service, keeping you informed, supported, and empowered throughout the legal process.</p></div>
  </div>
  <div class="pillar-divider" style="left:778px"></div>
  <div class="pillar" style="left:824px">
    <svg width="92" height="104" viewBox="0 0 92 104"><path d="M46 2 90 27v50L46 102 2 77V27z" fill="#d9b487"/><circle cx="46" cy="52" r="22" fill="none" stroke="#fff" stroke-width="2"/><rect x="22" y="45" width="48" height="14" fill="#fff"/><text x="46" y="56" text-anchor="middle" font-family="Montserrat,sans-serif" font-size="9" font-weight="800" fill="#d9b487">NO FEE</text></svg>
    <div><h3>NO WIN, NO FEE<br>GUARANTEE</h3><p>We take your case on a contingency basis, which means you pay nothing unless we win.</p></div>
  </div>
</section>

<section id="practice-areas">
  <h2 class="section-title practice-title">OUR <span class="gold">PRACTICE</span> AREAS</h2>
  <div class="practice-sub">Comprehensive Representation for the Injured</div>
  <div class="slider-btn" style="left:972px;background:var(--gold)"><svg width="10" height="10" viewBox="0 0 10 10"><path d="M6.5 1 2.5 5l4 4" stroke="#fff" stroke-width="1.8" fill="none"/></svg></div>
  <div class="slider-btn" style="left:1005px;background:var(--ink)"><svg width="10" height="10" viewBox="0 0 10 10"><path d="m3.5 1 4 4-4 4" stroke="#fff" stroke-width="1.8" fill="none"/></svg></div>

  <article class="card" style="left:165px">
    <div class="photo" role="img" aria-label="Damaged silver car after a collision" style="background:linear-gradient(135deg,#4d5a3e 0%,#8f9396 45%,#3d3f42 100%)"></div>
    <h3>CAR ACCIDENTS</h3>
    <p>We fight for victims of rear-end crashes, multi-vehicle collisions, pedestrian and cyclist accidents, and more.</p>
  </article>
  <article class="card" style="left:463px">
    <div class="photo" role="img" aria-label="Grieving woman in black beside a gravestone with flowers" style="background:linear-gradient(135deg,#6f7a5c 0%,#3b3c3e 50%,#9a9590 100%)"></div>
    <h3>WRONGFUL DEATH</h3>
    <p>We provide compassionate yet fierce representation for families who have lost a loved one due to negligence.</p>
  </article>
  <article class="card" style="left:760px">
    <div class="photo" role="img" aria-label="Person in a suit holding a product liability insurance document" style="background:linear-gradient(135deg,#2a2d31 0%,#55585c 40%,#e6e6e4 75%,#bdbcb8 100%)"></div>
    <h3>PRODUCT LIABILITY</h3>
    <p>If a dangerous product caused your injury, we pursue manufacturers, distributors, and retailers for maximum compensation.</p>
  </article>
</section>

<section id="florida-law">
  <div class="img-fill" role="img" aria-label="Bronze statue of blindfolded Lady Justice holding scales in front of courthouse columns" style="left:0;top:3300px;width:582px;height:493px;background:linear-gradient(135deg,#8a8579 0%,#3f3c37 45%,#26241f 70%,#6b675f 100%)"></div>
  <h2 class="section-title fl-title">FLORIDA PERSONAL<br><span class="gold">INJURY LAW</span>: WHAT YOU<br>NEED TO KNOW</h2>
  <div class="fl-sub">Your Rights and Legal Protections</div>

  <div class="law-item" style="top:3468px">
    <h3><svg width="16" height="16" viewBox="0 0 16 16"><circle cx="8" cy="8" r="7" fill="#2b2b2b"/><path d="m4.5 8 2.5 2.5 4.5-5" stroke="#fff" stroke-width="1.6" fill="none"/></svg>COMPARATIVE NEGLIGENCE (FLORIDA STATUTES §768.81)</h3>
    <p>Even if you were partially at fault, you can still recover compensation. Your damages will be reduced based on your percentage of fault.</p>
  </div>
  <div class="rule" style="top:3553px"></div>
  <div class="law-item" style="top:3574px">
    <h3><svg width="16" height="16" viewBox="0 0 16 16"><circle cx="8" cy="8" r="7" fill="#2b2b2b"/><path d="m4.5 8 2.5 2.5 4.5-5" stroke="#fff" stroke-width="1.6" fill="none"/></svg>STATUTE OF LIMITATIONS (FLORIDA STATUTES §95.11)</h3>
    <p>You have four years to file a personal injury claim and two years for wrongful death cases. Missing these deadlines can prevent you from recovering compensation.</p>
  </div>
  <div class="rule" style="top:3672px"></div>
  <div class="law-item" style="top:3697px">
    <h3><svg width="16" height="16" viewBox="0 0 16 16"><circle cx="8" cy="8" r="7" fill="#2b2b2b"/><path d="m4.5 8 2.5 2.5 4.5-5" stroke="#fff" stroke-width="1.6" fill="none"/></svg>PREMISES LIABILITY (FLORIDA STATUTES §768.0755)</h3>
    <p>Property owners are responsible for dangerous conditions they knew or should have known about.</p>
  </div>
</section>

<aside class="cta">
  <div class="cta-mark"><svg width="100" height="96" viewBox="0 0 100 96"><path d="M50 3 94 26v44L50 93 6 70V26z" fill="none" stroke="#fff" stroke-width="3"/></svg></div>
  <h2>TAKE THE FIRST STEP TOWARD JUSTICE</h2>
  <div class="tag">LET US FIGHT FOR THE COMPENSATION YOU DESERVE</div>
  <p>If you have been injured due to someone else's negligence, do not wait. Time-sensitive deadlines could impact your case.</p>
</aside>

<footer class="footer">
  <div class="foot-brand">
    <div class="name"><i></i>Darrow Law Firm</div>
    <div class="tagline">THE DARROW LAW FIRM: WHERE JUSTICE MEETS DEDICATION.</div>
  </div>
  <div class="foot-col foot-contact">
    <h4>CONTACT INFO</h4>
    <div class="row"><svg width="12" height="14" viewBox="0 0 12 14"><path d="M6 0a5 5 0 0 1 5 5c0 4-5 9-5 9S1 9 1 5a5 5 0 0 1 5-5z" fill="#d2a36f"/><circle cx="6" cy="5" r="1.8" fill="#303030"/></svg><div>Visit:<br>410 Ponce Lane, Coral Gables, FL 33134</div></div>
    <div class="row"><svg width="12" height="12" viewBox="0 0 24 24"><path d="M6.6 10.8a15 15 0 0 0 6.6 6.6l2.2-2.2a1 1 0 0 1 1-.25 11.4 11.4 0 0 0 3.6.57 1 1 0 0 1 1 1V20a1 1 0 0 1-1 1A17 17 0 0 1 3 4a1 1 0 0 1 1-1h3.5a1 1 0 0 1 1 1c0 1.25.2 2.45.57 3.6a1 1 0 0 1-.25 1z" fill="#d2a36f"/></svg><div>Call now:<br>(786) 555-0190</div></div>
    <div class="row"><svg width="12" height="12" viewBox="0 0 24 24"><path d="M2 5h20v14H2z" fill="#d2a36f"/><path d="m2 5 10 7 10-7" stroke="#303030" stroke-width="2" fill="none"/></svg><div>Email:<br>info@darrowlawfirm.com</div></div>
  </div>
  <div class="foot-col foot-links">
    <h4>THE DARROW LAW</h4>
    <div>Free Consultation</div>
    <div>No Fees Unless We Win</div>
    <div style="border-bottom:none">Aggressive Representation</div>
  </div>
  <div class="to-top"><svg width="14" height="16" viewBox="0 0 14 16"><path d="M7 15V2M2 7l5-5 5 5" stroke="#fff" stroke-width="1.6" fill="none"/></svg></div>
  <div class="copyright">© Copyright 2025, Darrow Law Firm, All Rights Reserved</div>
</footer>

</body>
</html>
```